Maple Ridge business card design

Card needs to include the following text/items:
Company Logo
Tobin Marsh
Phone # - 555-318-7642
service@mapleridgelandscaping.example
Lawn & landscape maintenance services

```html
<!DOCTYPE html>
<html lang="en">
<head>
<meta charset="utf-8">
<title>Maple Ridge Landscaping – Business Card</title>
<link rel="stylesheet" href="https://fonts.googleapis.com/css2?family=Cinzel:wght@400;700&family=EB+Garamond:wght@400;500&display=swap">
<style>
  :root {
    --backdrop: #b4b4b4;
    --card: #ffffff;
    --front-green: #6b8509;
    --back-green: #7f9a2f;
    --forest: #1f5a34;
    --ink: #111111;
    --white: #ffffff;
  }
  * { margin: 0; padding: 0; box-sizing: border-box; }
  html, body {
    width: 1200px;
    height: 1200px;
    overflow: hidden;
    background: var(--backdrop);
  }
  .canvas { position: relative; width: 1200px; height: 1200px; }
  .card {
    position: absolute;
    left: 135px;
    width: 930px;
    background: var(--card);
    overflow: hidden;
  }
  .card--front { top: 52px; height: 532px; }
  .card--back { top: 616px; height: 531px; }
  .card-shapes { position: absolute; inset: 0; width: 100%; height: 100%; }

  .brand-name {
    position: absolute;
    font-family: "Cinzel", serif;
    font-weight: 700;
    text-align: center;
    text-transform: uppercase;
    line-height: 1;
  }
  .brand-name .brand-sub { display: block; }
  .card--front .brand-name {
    left: 0; right: 0;
    top: 366px;
    color: var(--white);
    font-size: 62px;
  }
  .card--front .brand-name .brand-sub {
    font-size: 26px;
    letter-spacing: 22px;
    margin-top: 12px;
    margin-right: -22px;
  }
  .card--back .brand-name {
    left: 21px;
    width: 340px;
    top: 340px;
    color: var(--forest);
    font-size: 38px;
  }
  .card--back .brand-name .brand-sub {
    font-size: 17px;
    letter-spacing: 13px;
    margin-top: 8px;
    margin-right: -13px;
  }

  .tagline {
    position: absolute;
    left: 440px;
    width: 420px;
    top: 46px;
    font-family: "EB Garamond", serif;
    font-size: 31px;
    line-height: 36px;
    text-align: center;
    color: var(--ink);
  }
  .person-name {
    position: absolute;
    left: 454px;
    width: 387px;
    top: 186px;
    padding-bottom: 4px;
    border-bottom: 3px solid var(--ink);
    font-family: "Cinzel", serif;
    font-weight: 400;
    font-size: 52px;
    line-height: 56px;
    text-align: center;
    color: var(--back-green);
  }
  .phone {
    position: absolute;
    left: 440px;
    width: 420px;
    top: 266px;
    font-family: "EB Garamond", serif;
    font-size: 31px;
    text-align: center;
    color: var(--ink);
  }
  .email {
    position: absolute;
    left: 380px;
    width: 530px;
    top: 464px;
    font-family: "EB Garamond", serif;
    font-size: 26px;
    letter-spacing: 1px;
    text-align: center;
    color: var(--white);
  }
</style>
</head>
<body>
<main class="canvas">

  <section class="card card--front">
    <svg class="card-shapes" viewBox="0 0 930 532" aria-hidden="true">
      <circle class="brand-circle" cx="465" cy="212" r="152" fill="var(--forest)"/>
      <path class="ground-wave" fill="var(--front-green)"
        d="M0,373 C120,380 240,350 340,336 C420,326 520,330 600,346 C700,368 820,372 930,366 L930,532 L0,532 Z"/>
    </svg>
    <p class="brand-name">Maple Ridge<span class="brand-sub">Landscaping</span></p>
  </section>

  <section class="card card--back">
    <svg class="card-shapes" viewBox="0 0 930 531" aria-hidden="true">
      <path class="swoosh-top" fill="var(--back-green)"
        d="M210,0 L319,0 C375,60 412,140 412,215 C398,130 320,40 210,0 Z"/>
      <path class="swoosh-bottom" fill="var(--back-green)"
        d="M412,318 C402,420 320,500 207,531 L930,531 L930,429 C800,434 620,410 500,418 C430,424 390,445 365,464 C392,420 408,370 412,318 Z"/>
      <circle class="brand-circle" cx="191" cy="220" r="108" fill="var(--forest)"/>
    </svg>
    <p class="brand-name">Maple Ridge<span class="brand-sub">Landscaping</span></p>

    <p class="tagline">Lawn &amp; landscape<br>maintenance services</p>
    <h1 class="person-name">TOBIN MARSH</h1>
    <p class="phone">Contact #: 555-318-7642</p>
    <p class="email">service@mapleridgelandscaping.example</p>
  </section>

</main>
</body>
</html>
```